Yoga Shool offering Teacher Training in a new venue

I need to advertise our 200Hr Teacher Training course at the Brookfield Hall, I want to attract yoga students who want to be teachers as well as those looking to deepen their personal practice and attend for personal growth. I introduced yoga classes to this venue when it first opened in 2000, and I am returning with this Teacher Training course. My website colours are brown and orange.

Target Market(s)

Yoga Students around the venue

Font styles to use
Sans Serif

Colors

Designer to choose colors to be used in the design.

Requirements
Must have
• logo,

```html
<!DOCTYPE html>
<html lang="en">
<head>
<meta charset="utf-8">
<title>Tidal Yoga Teacher Training – Flyer</title>
<link href="https://fonts.googleapis.com/css2?family=Open+Sans:wght@300;400;600;700;800&display=swap" rel="stylesheet">
<style>
  :root {
    --orange: #e45c2a;
    --amber-top: #f8ad36;
    --amber-bottom: #f28a2b;
    --brown: #3f2826;
    --peach: #fde3c0;
    --speech: #fcdcb3;
    --ink: #2d2422;
    --white: #ffffff;
    --backdrop: #ece7e1;
  }
  * { box-sizing: border-box; margin: 0; padding: 0; }
  html, body {
    width: 1200px; height: 1000px; overflow: hidden;
    background: var(--backdrop);
    font-family: "Open Sans", Arial, sans-serif;
    color: var(--ink);
  }
  .canvas { position: relative; width: 1200px; height: 1000px; }
  .flyer {
    position: absolute; left: 264px; top: 27px;
    width: 764px; height: 1074px;
    transform: scale(0.88); transform-origin: top left;
    background: var(--white);
    overflow: hidden;
    box-shadow: 0 6px 18px rgba(0,0,0,.18);
  }
  .abs { position: absolute; }
  .hero-shape { left: 0; top: 0; width: 764px; height: 322px; }
  .hero-title {
    left: 44px; top: 48px; color: var(--white);
    line-height: .9; letter-spacing: -1px;
  }
  .hero-title .light { font-weight: 300; font-size: 84px; display: block; }
  .hero-title .bold { font-weight: 800; font-size: 86px; display: block; margin-top: 4px; }
  .brand-mark {
    left: 257px; top: 57px; width: 124px; height: 124px; border-radius: 50%;
    background: var(--brown); color: var(--orange);
    display: flex; align-items: center; justify-content: center; text-align: center;
    font-weight: 800; font-size: 22px; line-height: 1.05;
  }
  .course-column {
    left: 44px; top: 297px; width: 319px; height: 777px;
    background: linear-gradient(180deg, var(--amber-top) 0%, var(--amber-bottom) 40%, var(--orange) 100%);
  }
  .tagline {
    left: 44px; top: 304px; width: 319px; text-align: center;
    font-weight: 700; font-size: 23px; line-height: 1.28; color: var(--ink);
  }
  .course-title { left: 44px; top: 392px; width: 319px; text-align: center; }
  .course-title .brand { font-weight: 300; font-size: 31px; letter-spacing: 2px; color: var(--ink); display: block; }
  .course-title .program { font-weight: 800; font-size: 44px; line-height: 1; color: var(--orange); display: block; margin-top: 6px; }
  .course-title .coming { font-weight: 300; font-size: 25px; letter-spacing: 1.5px; color: var(--ink); display: block; margin-top: 2px; }
  .course-title .venue { font-weight: 700; font-size: 24px; color: var(--ink); display: block; margin-top: -2px; }
  .photo-circle { left: 62px; top: 602px; width: 280px; height: 187px; background: linear-gradient(135deg, #6d8a4a, #a48670 50%, #5e7a3c); }
  .photo-teacher { left: 62px; top: 797px; width: 280px; height: 277px; background: linear-gradient(180deg, #4f7a3a, #7fa35a 55%, #6e5a48); }
  .intro-panel { left: 363px; top: 360px; width: 401px; height: 248px; background: var(--peach); }
  .intro-lead { left: 381px; top: 373px; font-size: 25px; font-weight: 300; color: var(--orange); }
  .intro-lead strong { font-weight: 700; }
  .intro-questions { left: 381px; top: 407px; width: 360px; font-size: 17.5px; line-height: 1.22; color: var(--ink); }
  .intro-questions strong { font-weight: 700; }
  .intro-callout { left: 381px; top: 476px; font-size: 24px; font-weight: 800; color: var(--orange); }
  .intro-body { left: 381px; top: 514px; width: 345px; font-size: 13.5px; line-height: 1.25; color: var(--ink); }
  .speech { left: 372px; top: 620px; width: 336px; height: 98px; }
  .speech-text { left: 381px; top: 629px; width: 320px; font-size: 16.5px; font-weight: 700; line-height: 1.18; color: var(--ink); }
  .testimonials { left: 383px; top: 726px; width: 345px; font-size: 13.8px; line-height: 1.2; color: var(--ink); }
  .testimonial { margin-bottom: 15px; }
  .testimonial cite { display: block; font-style: normal; font-weight: 700; }
  .details-note { left: 384px; top: 979px; font-size: 17px; color: var(--ink); }
  .footer-band { left: 0; top: 1007px; width: 764px; height: 67px; background: var(--orange); }
  .course-column-foot { left: 44px; top: 1007px; width: 319px; height: 67px; background: var(--orange); }
  .website { left: 385px; top: 1017px; font-size: 25px; font-weight: 700; color: var(--white); }
</style>
</head>
<body>
<main class="canvas">
  <article class="flyer">
    <svg class="abs hero-shape" viewBox="0 0 764 322" aria-hidden="false">
      <polygon points="0,0 297,0 415,322 0,322" fill="var(--orange)"/>
      <polygon points="297,0 764,0 764,322 415,322" fill="#3d7fa8" role="img" aria-label="Photo: yogi in a headstand on a beach by the sea"/>
      <defs>
        <linearGradient id="sea-sand" x1="0" y1="0" x2="0" y2="1">
          <stop offset="0" stop-color="#2f6f9a"/>
          <stop offset=".55" stop-color="#6aa1bf"/>
          <stop offset=".7" stop-color="#d9d3c8"/>
          <stop offset="1" stop-color="#b49b7e"/>
        </linearGradient>
      </defs>
      <polygon points="297,0 764,0 764,322 415,322" fill="url(#sea-sand)"/>
    </svg>

    <h1 class="abs hero-title">
      <span class="light">ARE<br>YOU</span>
      <span class="bold">READY?</span>
    </h1>

    <div class="abs brand-mark">Tidal<br>Yoga</div>

    <div class="abs course-column"></div>
    <p class="abs tagline">Set in motion a stunning transformation in 2019</p>

    <h2 class="abs course-title">
      <span class="brand">TIDAL YOGA</span>
      <span class="program">TEACHER<br>TRAINING</span>
      <span class="coming">is coming to</span>
      <span class="venue">BROOKFIELD HALL</span>
    </h2>

    <div class="abs photo-circle" role="img" aria-label="Photo: group of students joining hands in a circle on the grass"></div>
    <div class="abs photo-teacher" role="img" aria-label="Photo: yoga teacher seated on a bench in a garden"></div>

    <div class="abs intro-panel"></div>
    <p class="abs intro-lead">Do you love <strong>Yoga?</strong></p>
    <p class="abs intro-questions">Do you want to know yourself,<br><strong>love</strong> yourself, <strong>heal</strong> yourself and<br><strong>treat yourself better?</strong></p>
    <p class="abs intro-callout">THIS IS FOR YOU!</p>
    <p class="abs intro-body">Tidal Yoga Teacher Training isn’t just for aspiring teachers, it’s for any dedicated student of yoga to build a powerful personal practice and deepen their understanding and experience of yoga.</p>

    <svg class="abs speech" viewBox="0 0 336 98" aria-hidden="true">
      <path d="M0 0 H336 V78 H290 L278 98 L266 78 H0 Z" fill="var(--speech)"/>
    </svg>
    <p class="abs speech-text">Take the next step in your yoga and in your life, access new possibilities, check out what past trainees had to say:</p>

    <div class="abs testimonials">
      <blockquote class="testimonial">“Wow! This course has been life changing in every way, it has given me so much confidence to do things I haven’t done before.”<cite>— Jo Marlow, 2018</cite></blockquote>
      <blockquote class="testimonial">“I love how we apply everything to our own lives — it’s real and tangible, so we live it and learn it...”<cite>— Ellis Grant Ward, 2016</cite></blockquote>
      <blockquote class="testimonial">“I loved every lesson, and as I applied the teachings to my life, they had a flow on effect to my family too. Prepare to not only become a yoga teacher, prepare to change in incredibly positive ways.”<cite>— Nina Carvel, 2018</cite></blockquote>
    </div>

    <p class="abs details-note">Course Details are available on our website:</p>

    <div class="abs footer-band"></div>
    <div class="abs photo-teacher" role="img" aria-label="Photo: yoga teacher seated on a bench in a garden" style="z-index:1"></div>
    <p class="abs website">www.tidalyoga.com.au</p>
  </article>
</main>
</body>
</html>
```